Pediatric Dentist Business Card

I need a business card designed for a dentist who works exclusively with children.
We prefer designs that are out of ordiary that is fun and interesting to kids.

there is no logo since this is a dentists office. The name of the doctor is "Tavor Kesh" if you want to get creative with that.

Target Market(s)

Kids

Industry/Entity Type

Business

Contact Information for Business Card

Anythings that is creative

Colors

Designer to choose colors to be used in the design.

```html
<!DOCTYPE html>
<html lang="en">
<head>
<meta charset="utf-8">
<title>Brightbite Pediatric Dentistry – Business Card</title>
<link rel="stylesheet" href="https://fonts.googleapis.com/css2?family=Montserrat:wght@400;500;600;700;800&display=swap">
<style>
  :root {
    --navy: #144a5e;
    --cyan: #35bcdf;
    --cyan-faint: #d9f1f9;
    --white: #ffffff;
    --ink: #174b5f;
    --grey: #9a9a9a;
    --page: #e9ecee;
  }
  * { margin: 0; padding: 0; box-sizing: border-box; }
  html, body { width: 1200px; height: 900px; overflow: hidden; }
  body {
    background: var(--page);
    font-family: "Montserrat", sans-serif;
    position: relative;
  }
  .card {
    position: absolute;
    left: 290px;
    width: 620px;
    height: 354px;
    border-radius: 18px;
    overflow: hidden;
    background: var(--white);
    box-shadow: 0 6px 18px rgba(0,0,0,0.12);
  }
  .card--front { top: 70px; }
  .card--back { top: 476px; }

  /* Front */
  .front__top { position: absolute; left: 0; top: 0; width: 100%; height: 84px; background: var(--navy); }
  .front__bottom { position: absolute; left: 0; bottom: 0; width: 100%; height: 122px; background: var(--cyan); }
  .front__brand { position: absolute; left: 60px; top: 108px; display: flex; align-items: center; gap: 26px; }
  .brand-dot { width: 100px; height: 100px; border-radius: 50%; background: var(--cyan); flex: none; }
  .brand-name { font-weight: 600; font-size: 46px; color: var(--ink); letter-spacing: -0.5px; }
  .front__web { position: absolute; left: 0; right: 0; bottom: 46px; text-align: center; color: var(--white); font-weight: 600; font-size: 21px; letter-spacing: 0.3px; }

  /* Back */
  .back__art { position: absolute; left: 0; top: 0; width: 620px; height: 354px; }
  .back__brand { position: absolute; left: 28px; top: 66px; display: flex; align-items: center; gap: 16px; }
  .back__brand .brand-dot { width: 60px; height: 60px; background: var(--white); }
  .back__brand .brand-name { font-size: 27px; color: var(--white); }
  .back__person { position: absolute; left: 44px; top: 184px; }
  .person-name { font-weight: 800; font-size: 30px; color: var(--ink); line-height: 1; }
  .person-title { font-weight: 600; font-size: 15px; color: var(--cyan); margin: 4px 0 6px 14px; line-height: 1.2; }
  .contact-list { list-style: none; margin-left: 26px; }
  .contact-list li { font-weight: 500; font-size: 17px; color: var(--grey); line-height: 1.15; }
</style>
</head>
<body>
  <section class="card card--front" aria-label="Business card front">
    <div class="front__top"></div>
    <div class="front__brand">
      <span class="brand-dot"></span>
      <span class="brand-name">Brightbite</span>
    </div>
    <div class="front__bottom"></div>
    <p class="front__web">www.brightbitekids.com</p>
  </section>

  <section class="card card--back" aria-label="Business card back">
    <svg class="back__art" viewBox="0 0 620 354" aria-hidden="true">
      <circle cx="600" cy="150" r="170" fill="var(--cyan-faint)"/>
      <polygon points="0,0 620,0 620,60 0,162" fill="var(--navy)"/>
      <polygon points="0,162 620,60 620,70 0,172" fill="var(--cyan)"/>
      <rect x="0" y="334" width="620" height="20" fill="var(--cyan)"/>
    </svg>
    <div class="back__brand">
      <span class="brand-dot"></span>
      <span class="brand-name">Brightbite</span>
    </div>
    <div class="back__person">
      <h1 class="person-name">Tavor Kesh</h1>
      <p class="person-title">Title</p>
      <ul class="contact-list">
        <li>Address</li>
        <li>www.brightbitekids.com</li>
        <li>555-014-288</li>
        <li>hello@brightbitekids.com</li>
      </ul>
    </div>
  </section>
</body>
</html>
```